A gang member and street hustler turned preacher needs a cover

A man who used to be a gang member and street hustler turned his life around and became a preacher. He has written a book titled Unsteepled: My Passage From Ashes to Glory and he needs a cover for the book. The book is a memoir about his life and his journey from the streets to the church. It details the lessons that he's learned along the way. I have attached a photo to incorporate in the cover design. <br/>Title: Unsteepled: My Passage From Ashes to Glory<br/>Author: Dr. Marlon T. Grady

```html
<!DOCTYPE html>
<html lang="en">
<head>
<meta charset="utf-8">
<title>Unsteepled — Book Cover</title>
<link rel="stylesheet" href="https://fonts.googleapis.com/css2?family=Caladea:wght@400;700&family=Open+Sans:wght@400;600&display=swap">
<style>
  :root {
    --page-bg: #e9e9e9;
    --cover-bg: #ffffff;
    --ink-bronze: #6c5e4f;
    --ink-bronze-dark: #4d4236;
    --rule: #3a332c;
    --splatter: rgba(150, 150, 150, 0.22);
    --iron-light: #6a6150;
    --iron-dark: #2f2a22;
  }
  * { margin: 0; padding: 0; box-sizing: border-box; }
  html, body {
    width: 1200px;
    height: 840px;
    overflow: hidden;
    background: var(--page-bg);
  }
  .canvas {
    position: relative;
    width: 1200px;
    height: 840px;
  }
  .cover {
    position: absolute;
    left: 344px;
    top: 40px;
    width: 512px;
    height: 760px;
    background: var(--cover-bg);
    overflow: hidden;
    box-shadow: 0 2px 10px rgba(0,0,0,0.12);
  }
  .cover__wash {
    position: absolute;
    inset: 0;
    background:
      radial-gradient(ellipse 180px 140px at 470px 60px, var(--splatter), transparent 70%),
      radial-gradient(ellipse 160px 90px at 300px 20px, rgba(150,150,150,0.12), transparent 70%),
      radial-gradient(ellipse 220px 70px at 360px 740px, var(--splatter), transparent 70%),
      radial-gradient(ellipse 160px 60px at 110px 735px, rgba(150,150,150,0.15), transparent 70%);
  }
  .cover__author {
    position: absolute;
    top: 126px;
    left: 0;
    width: 100%;
    text-align: center;
    font-family: "Open Sans", sans-serif;
    font-weight: 600;
    font-size: 26px;
    color: var(--ink-bronze);
    letter-spacing: 0.2px;
  }
  .cover__title {
    position: absolute;
    top: 200px;
    left: 0;
    width: 100%;
    text-align: center;
    font-family: "Caladea", serif;
    font-weight: 700;
    font-size: 60px;
    line-height: 1;
    color: var(--ink-bronze);
    background: linear-gradient(180deg, #8a7c6c 0%, var(--ink-bronze) 45%, var(--ink-bronze-dark) 100%);
    -webkit-background-clip: text;
    background-clip: text;
    -webkit-text-fill-color: transparent;
    letter-spacing: 0.5px;
  }
  .cover__rule {
    position: absolute;
    top: 272px;
    left: 36px;
    width: 442px;
    height: 1.5px;
    background: var(--rule);
  }
  .cover__subtitle {
    position: absolute;
    top: 283px;
    left: 0;
    width: 100%;
    text-align: center;
    font-family: "Open Sans", sans-serif;
    font-weight: 400;
    font-size: 25px;
    color: var(--ink-bronze);
  }
  .cover__artwork {
    position: absolute;
    top: 370px;
    left: 55px;
    width: 400px;
    height: 250px;
    border-radius: 40px;
    background: radial-gradient(ellipse at 50% 45%, var(--iron-light) 0%, var(--iron-dark) 75%, rgba(47,42,34,0) 100%);
  }
</style>
</head>
<body>
  <main class="canvas">
    <section class="cover">
      <div class="cover__wash" aria-hidden="true"></div>
      <p class="cover__author">Dr. Marlon T. Grady</p>
      <h1 class="cover__title">UNSTEEPLED</h1>
      <div class="cover__rule" aria-hidden="true"></div>
      <p class="cover__subtitle">My Passage From Ashes to Glory</p>
      <div class="cover__artwork" role="img" aria-label="Photograph of a pair of open, rusted iron shackles joined by a chain"></div>
    </section>
  </main>
</body>
</html>
```